Brochure Design Project - Innovative Service for Pharma Industry

Our start up is based in Germany, near Munich and we provide an innovative Service for the pharma industry. We develop product trainings and general trainings online. The adressed audience for these trainings are pharmacies and medics. The parma industry could increase the number of trainings, while saving money (incl a success guarantee). Our (not yet finnished) corporate page can be reviewed here: www.brevoloq.biz, our 'product & service' page is www.kestrumlearn.com. The color code should be leaned towards the corporate page.

The brochure should be send to decision makers in the pharma industry and rise the interest in innovative service. Seriousity should meet modern & clear design.Something eye cathing on the front page might be required.

Target Market(s)

Usually more conservative decision makers within the pharma industry

Industry/Entity Type

Industry

Requirements
Must have
• Conceptional design for an brochure (Din A4 size) of approx 6-8 pages, that capture the key messages (exact content would be filled / provided from us)
Nice to have
• Implementing some of the pics / phrases on the home page www.brevolq.biz could be maybe nice. How about a personal statement from the founder combined with a pic(pic attached)? Both is no must....

```html
<!DOCTYPE html>
<html lang="en">
<head>
<meta charset="utf-8">
<title>Brevoloq Brochure 2013 – Cover Spread</title>
<link rel="stylesheet" href="https://fonts.googleapis.com/css2?family=Open+Sans:wght@400;600&family=Carlito:ital,wght@0,400;1,400&family=Orbitron:wght@900&display=swap">
<style>
  :root {
    --page-bg: #e9e6e2;
    --paper: #ffffff;
    --top-bar: #4a4a4a;
    --red-top: #c9290b;
    --red-mid: #6e1407;
    --red-bottom: #120302;
    --fold-line: #2a0602;
    --brand-orange: #e4521f;
    --accent-orange: #ef3f16;
    --bubble: #d58a6c;
    --photo-light: #8fb8cf;
    --photo-dark: #2f4658;
    --text-light: #ffffff;
  }
  * { margin: 0; padding: 0; box-sizing: border-box; }
  html, body {
    width: 1200px; height: 960px; overflow: hidden;
    background: var(--page-bg);
  }
  .spread {
    position: absolute; left: 47px; top: 84px;
    width: 1116px; height: 790px;
    background: var(--paper);
    box-shadow: 0 6px 18px rgba(0,0,0,0.25);
    overflow: hidden;
  }
  .top-bar {
    position: absolute; left: 0; top: 0; width: 100%; height: 26px;
    background: var(--top-bar);
  }
  .cover-field {
    position: absolute; left: 0; top: 120px; width: 1116px; height: 636px;
  }
  .brand {
    position: absolute; display: flex; align-items: center; gap: 6px;
    font-family: "Open Sans", sans-serif; font-weight: 600;
    color: var(--brand-orange); font-size: 22px; letter-spacing: 0.5px;
    transform: translate(-50%, -50%);
  }
  .brand-dot {
    width: 11px; height: 11px; border-radius: 50%;
    background: var(--brand-orange);
  }
  .brand--header { left: 624px; top: 75px; }
  .brand--back { left: 279px; top: 422px; }
  .back-url {
    position: absolute; left: 279px; top: 451px; transform: translate(-50%, -50%);
    font-family: "Open Sans", sans-serif; font-size: 14px; color: var(--text-light);
  }
  .quote-photo {
    position: absolute; left: 595px; top: 403px; width: 302px; height: 240px;
    border-radius: 20px; overflow: hidden;
    background: radial-gradient(ellipse at 45% 60%, #c9a48f 0%, var(--photo-light) 45%, var(--photo-dark) 100%);
  }
  .quote {
    position: absolute; right: 13px; top: 6px; text-align: right;
    font-family: "Carlito", sans-serif; font-size: 12.5px; line-height: 14px;
    color: var(--text-light);
  }
  .quote-source {
    display: block; margin-top: 14px; margin-right: 3px;
    font-style: italic; font-size: 11.5px;
  }
  .edition-title {
    position: absolute; left: 876px; top: 690px;
    font-family: "Orbitron", sans-serif; font-weight: 900; font-size: 18px;
    letter-spacing: 1.5px; color: var(--accent-orange);
  }
</style>
</head>
<body>
  <main class="spread">
    <div class="top-bar"></div>

    <div class="brand brand--header"><span class="brand-name">brevoloq</span><span class="brand-dot"></span></div>

    <svg class="cover-field" width="1116" height="636" viewBox="0 0 1116 636" aria-hidden="true">
      <defs>
        <linearGradient id="coverRed" x1="0" y1="0" x2="0" y2="1">
          <stop offset="0" stop-color="var(--red-top)"/>
          <stop offset="0.5" stop-color="var(--red-mid)"/>
          <stop offset="1" stop-color="var(--red-bottom)"/>
        </linearGradient>
      </defs>
      <path d="M0 0 H1116 V635 Q558 575 0 635 Z" fill="url(#coverRed)"/>
      <line x1="559" y1="0" x2="559" y2="604" stroke="var(--fold-line)" stroke-width="1"/>
      <circle cx="1077" cy="47" r="16" fill="var(--bubble)" opacity="0.85"/>
      <circle cx="1005" cy="90" r="40" fill="var(--bubble)" opacity="0.85"/>
      <circle cx="905" cy="196" r="74" fill="var(--bubble)" opacity="0.85"/>
    </svg>

    <div class="brand brand--back"><span class="brand-name">brevoloq</span><span class="brand-dot"></span></div>
    <p class="back-url">http://brevoloq.biz/</p>

    <figure class="quote-photo" role="img" aria-label="Photo of a person framing the view with both hands">
      <blockquote class="quote">„If you always do what you always did,<br>you always get what you always got“
        <cite class="quote-source">ANONYM</cite>
      </blockquote>
    </figure>

    <h1 class="edition-title">BROCHURE 2013</h1>
  </main>
</body>
</html>
```